Bright and beautiful business card for a coach

I'm a personal and business coach based in Perth, Australia. I need a business card that whilst subtle and elegant, will stand out and appeal on a table full of cards.

My business name is Tide Mentoring and the business card must represent the warmth and brightness implied in the name, without being gimmicky. It must have a warmth and appeal and be easy to read.

I prefer clean, minimalist designs.

It must align with the feel of my website and socials: https://www.tidementoring.com.au/
https://www.instagram.com/tidementoringau/
https://www.facebook.com/tidementoringau
Updates

Hi Designers Thank you so much for taking the time to submit designs. I wonder if I could have explained myself a little better. Most of the designs that have been submitted look rather formal and many have quite corporate looking embellishments on them (to my eye). I would like softer, warmer, more organic. I’m open to people playing about and being more abstract, using softer embellishments (e.g the line drawing flowers and grasses I’ve used in my socials) incorporating other colours from my palette or like the social icons in my email signature (in PDF), perhaps playing with size/oversize, playing with the bleed. Please don’t be constrained by what I’ve already done, it merely needs to compliment. I’m sorry if I’m not using the right words or have led you astray. I’m no designer, but I’ve done my website, socials, email signature etc all myself (my logo was a design contest) and I was really hoping for my business card to be something more creative than I could have made with a template. Reminder: No black cards/sides please. Thank you 😊

Target Market(s)

Individuals, most likely but not all female. Creative thinkers. Likely professionals.

Industry/Entity Type

Business & Personal Coach

Contact Information for Business Card

(Tide Mentoring Logo) Name: Maren Delsby; Title: Business & Personal Coach; Phone number: +61 (0)438 915307; Email: maren@tidementoring.com.au; Website: https://tidementoring.com.au; Social icons for Facebook, Instagram & LinkedIn: @tidementoringAU. Optional strapline: "A thinking partner to help you cut through the noise"

Font styles to use
Sans Serif

Colors
00AB8E
00BBA5
67D7C9
C6EFE9
E9F9F6
59FF00
82FF00
B8FF75
E3FFCB
F4FFEA
FFC000
F8CF3A
FAE287
FDF2CF
FEFAEE

Requirements
Must have
• Must align with feel of my website and socials. Must have a pop of #FFC000 (possibly whole of one side, or at least a block). Bright or white background. Easy to read.
Nice to have
• Possibly incorporate the sunshine/grass picture I have used in website and socials - will upload.
Should not have
• Must not be black or dark. Not impersonal or corporate looking.

```html
<!DOCTYPE html>
<html lang="en">
<head>
<meta charset="utf-8">
<title>Tide Mentoring – Business Card</title>
<link rel="stylesheet" href="https://fonts.googleapis.com/css2?family=Josefin+Sans:wght@300;400;600&display=swap">
<style>
  :root {
    --backdrop: #e6e0d7;
    --paper: #f2f1ee;
    --sun: #ffc000;
    --sun-soft: #f8cf3a;
    --sun-pale: #fae287;
    --sun-mist: #fdf2cf;
    --mint: #c6efe9;
    --aqua: #67d7c9;
    --sea: #00bba5;
    --teal-name: #5fb8a8;
    --teal-icon: #a9d9d0;
    --slate: #56666a;
    --logo-grey: #858585;
  }
  * { margin: 0; padding: 0; box-sizing: border-box; }
  html, body { width: 1200px; height: 1200px; overflow: hidden; }
  body {
    background: var(--backdrop);
    font-family: "Josefin Sans", sans-serif;
    position: relative;
  }
  .card {
    position: absolute;
    left: 249px;
    width: 702px;
    height: 401px;
    background: var(--paper);
    overflow: hidden;
  }
  .card--front { top: 176px; }
  .card--back { top: 651px; }
  .card__shapes {
    position: absolute; inset: 0;
    width: 100%; height: 100%;
  }
  .brand {
    position: absolute;
    left: 0; right: 0;
    top: 178px;
    display: flex;
    align-items: center;
    justify-content: center;
    gap: 16px;
  }
  .brand__dot {
    width: 26px; height: 26px;
    border-radius: 50%;
    background: var(--sun);
  }
  .brand__name {
    font-weight: 600;
    font-size: 34px;
    letter-spacing: 9px;
    text-transform: uppercase;
    color: var(--logo-grey);
  }
  .person__name {
    position: absolute;
    left: 50px; top: 62px;
    font-weight: 400;
    font-size: 54px;
    line-height: 1;
    letter-spacing: 0.5px;
    text-transform: uppercase;
    color: var(--teal-name);
  }
  .person__title {
    position: absolute;
    left: 51px; top: 124px;
    font-weight: 400;
    font-size: 20px;
    letter-spacing: 3.4px;
    text-transform: uppercase;
    color: var(--slate);
  }
  .contact {
    position: absolute;
    left: 51px; top: 195px;
    list-style: none;
  }
  .contact__item {
    display: flex;
    align-items: center;
    gap: 14px;
    height: 28px;
    margin-bottom: 10.5px;
    font-weight: 300;
    font-size: 21px;
    letter-spacing: 0.5px;
    color: var(--slate);
  }
  .contact__item--phone { letter-spacing: 2px; }
  .contact__item--caps { text-transform: uppercase; }
  .contact__icon {
    width: 28px; height: 28px;
    border-radius: 50%;
    background: var(--teal-icon);
    display: flex;
    align-items: center;
    justify-content: center;
    flex: none;
  }
  .contact__icon svg { width: 15px; height: 15px; }
  .social {
    position: absolute;
    left: 138px; top: 311px;
    display: flex;
    gap: 13.5px;
  }
  .social__dot {
    width: 28px; height: 28px;
    border-radius: 50%;
    background: var(--teal-icon);
  }
  .social__handle {
    position: absolute;
    left: 94px; top: 346px;
    font-weight: 300;
    font-size: 21px;
    letter-spacing: 0.5px;
    text-transform: uppercase;
    color: var(--slate);
  }
</style>
</head>
<body>

<section class="card card--front" aria-label="Card front">
  <svg class="card__shapes" viewBox="0 0 702 401" aria-hidden="true">
    <circle cx="40" cy="20" r="95" fill="var(--mint)"/>
    <circle cx="150" cy="-10" r="38" fill="var(--sun-mist)"/>
    <circle cx="690" cy="60" r="52" fill="var(--sun-pale)"/>
    <path fill="var(--aqua)" opacity="0.55" d="M0 330 C90 300 170 360 260 345 C330 333 370 370 400 401 H0 Z"/>
    <path fill="var(--mint)" d="M0 360 C80 345 150 385 230 375 C290 368 320 390 335 401 H0 Z"/>
    <circle cx="702" cy="401" r="150" fill="var(--sun)"/>
    <circle cx="702" cy="401" r="95" fill="var(--sun-soft)"/>
  </svg>
  <div class="brand">
    <span class="brand__dot"></span>
    <span class="brand__name">Tide Mentoring</span>
  </div>
</section>

<section class="card card--back" aria-label="Card back">
  <svg class="card__shapes" viewBox="0 0 702 401" aria-hidden="true">
    <rect x="0" y="0" width="702" height="22" fill="var(--sun)"/>
    <circle cx="702" cy="0" r="120" fill="var(--sun-pale)"/>
    <circle cx="702" cy="0" r="70" fill="var(--sun)"/>
    <circle cx="702" cy="401" r="135" fill="var(--mint)"/>
    <circle cx="640" cy="330" r="22" fill="var(--aqua)" opacity="0.6"/>
    <path fill="var(--sun-mist)" d="M0 384 C120 372 240 392 360 384 C450 378 520 390 580 401 H0 Z"/>
  </svg>

  <h1 class="person__name">Maren Delsby</h1>
  <p class="person__title">Business &amp; Personal Coach</p>

  <ul class="contact">
    <li class="contact__item contact__item--phone">
      <span class="contact__icon">
        <svg viewBox="0 0 24 24"><path fill="var(--slate)" d="M6.6 10.8c1.4 2.8 3.8 5.1 6.6 6.6l2.2-2.2c.3-.3.7-.4 1-.2 1.1.4 2.3.6 3.6.6.6 0 1 .4 1 1V20c0 .6-.4 1-1 1C10.6 21 3 13.4 3 4c0-.6.4-1 1-1h3.5c.6 0 1 .4 1 1 0 1.3.2 2.5.6 3.6.1.3 0 .7-.2 1l-2.3 2.2z"/></svg>
      </span>
      +61 (0)438 915307
    </li>
    <li class="contact__item contact__item--caps">
      <span class="contact__icon">
        <svg viewBox="0 0 24 24"><rect x="3" y="6" width="18" height="12" fill="var(--slate)"/><path d="M3 6 L12 13 L21 6" fill="none" stroke="var(--teal-icon)" stroke-width="1.5"/></svg>
      </span>
      maren@tidementoring.com.au
    </li>
    <li class="contact__item contact__item--caps">
      <span class="contact__icon">
        <svg viewBox="0 0 24 24" fill="none" stroke="var(--slate)" stroke-width="1.6"><circle cx="12" cy="12" r="9"/><ellipse cx="12" cy="12" rx="4" ry="9"/><path d="M3 12h18M5 7.5h14M5 16.5h14"/></svg>
      </span>
      tidementoring.com.au
    </li>
  </ul>

  <div class="social" aria-label="Social channels">
    <span class="social__dot"></span>
    <span class="social__dot"></span>
    <span class="social__dot"></span>
  </div>
  <p class="social__handle">@tidementoringAU</p>
</section>

</body>
</html>
```